Brightfold Partners Website

Brightfold Partners Advisory Services is a company which provides specialised advise in carbon markets, climate policy, landscapes, resilience and change. We are based in Australia but the majority of our business is global. Our clients range from governments to large corporates and not for profit organisations.
Our focus is on developing the capabilities of government officials, business decision makers and land managers so they can better navigate the complexity of climate change and sustainability.
We are looking for a website that is consistent with the high end professional services which we provide to serious players.
I have attached two versions of our logo. I have also attached the back of our business card so you can get a sense of what we hand to potential clients.

Target Market(s)

Professional individuals, decision makers, board members etc, government officials.

Industry/Entity Type

Government

Number of Pages Required

4 page

Font styles to use
Serif
Sans Serif

Requirements
Must have
• Please provide
• 1. Home page
• 2. Service page template
• 3. Contact page
• 4. Lead expert profile page

```html
<!DOCTYPE html>
<html lang="en">
<head>
<meta charset="utf-8">
<title>Brightfold Partners</title>
<link rel="stylesheet" href="https://fonts.googleapis.com/css2?family=Merriweather:wght@300;400&family=Playfair+Display:wght@400&display=swap">
<style>
:root{
  --blue:#0b78d8;
  --ink:#1b2832;
  --footer:#1d2b35;
  --footer-deep:#141e25;
  --text:#333a40;
  --muted:#8b959c;
  --rule:#d6dadd;
  --panel:#efefef;
  --white:#ffffff;
  --field:#ffffff;
}
*{box-sizing:border-box;margin:0;padding:0}
html,body{width:1200px;height:2691px;overflow:hidden}
body{position:relative;background:var(--white);font-family:"Merriweather",Georgia,serif;font-weight:300;color:var(--text)}
.abs{position:absolute}

.top-strip{left:0;top:0;width:1200px;height:9px;background:var(--ink)}
.header{left:0;top:9px;width:1200px;height:126px;background:var(--white)}
.brand{left:45px;top:36px;display:flex;align-items:center;gap:14px}
.brand-mark{width:50px;height:50px;border-radius:50%;background:#6f7a82}
.brand-name{font-family:"Playfair Display",Georgia,serif;font-size:31px;line-height:30px;letter-spacing:3px;color:#3c4347;text-transform:uppercase}
.contact-line{right:45px;font-size:13px;color:var(--muted);display:flex;align-items:center;gap:10px}
.nav{right:45px;top:68px;display:flex;font-size:15px;color:var(--ink)}
.nav a{display:block;padding:0 12px;height:33px;line-height:33px;color:inherit;text-decoration:none}
.nav a.active{background:var(--blue);color:var(--white)}

.hero{left:0;top:135px;width:1200px;height:523px;background:linear-gradient(170deg,#8b9299 0%,#c8ccd0 35%,#6c7f91 65%,#2c2f33 100%)}
.hero-card{left:768px;top:213px;width:385px;height:320px;background:var(--blue);color:var(--white)}
.hero-card p{position:absolute;left:60px;top:62px;width:310px;font-size:22px;line-height:31px;font-weight:300}
.hero-card p b{font-size:32px;font-weight:400;font-style:italic}
.dots{right:10px;bottom:10px;display:flex;gap:4px}
.dots i{width:10px;height:10px;background:#8ec2f0}
.dots i.on{background:#0d2b47}
.hero-profile{left:768px;top:533px;width:385px;height:82px;background:rgba(27,40,50,.85);color:#d5dbe0;font-size:13px;line-height:18px}
.hero-profile .portrait{position:absolute;left:4px;top:4px;width:72px;height:74px;background:linear-gradient(#c9a58c,#52606b)}
.hero-profile p{position:absolute;left:97px;top:22px}
.hero-profile u{color:#e8ecef}

.section-rule{left:45px;width:1108px;height:1px;background:var(--rule)}
.section-label{height:32px;line-height:32px;background:var(--blue);color:var(--white);font-size:20px;text-align:center}
.mission-text{left:70px;top:760px;width:1060px;font-size:14px;line-height:21.5px;text-align:center;color:#2d3338}
.btn-ghost{height:27px;line-height:25px;border:1px solid #d0d4d7;font-size:12.5px;color:var(--muted);text-align:center;background:var(--white)}

.card{width:350px;height:202px;background:var(--ink);color:var(--white)}
.card .photo{height:116px}
.card h3{position:absolute;left:24px;top:116px;height:86px;display:flex;align-items:center;font-weight:300;font-size:16px;line-height:22px}
.card.active{background:var(--blue)}

.news-photo{width:131px;height:213px}
.news-body{width:325px;font-size:14.5px;line-height:21.5px;color:#2d3338}
.news-body h4{font-weight:300;font-size:17px;margin-bottom:10px;color:#222}
.news-body .btn-ghost{margin-top:14px;width:116px}

.contact{left:0;top:1921px;width:1200px;height:391px;background:var(--panel)}
.field-label{font-size:12.5px;color:#222}
.field{background:var(--field);border:1px solid #d6d9dc}
.btn-dark{background:var(--ink);color:var(--white);font-size:15px;text-align:center;height:32px;line-height:32px}

.footer{left:0;top:2312px;width:1200px;height:253px;background:var(--footer);color:#8c98a1;font-size:13px;line-height:21px}
.footer h5{font-weight:300;font-size:13.5px;color:#c9d0d5;border-bottom:1px solid #3d4b55;padding-bottom:3px;margin-bottom:10px;display:inline-block}
.footer ul{list-style:none}
.footer .brand-name{color:#dfe4e8}
.socials{display:flex;gap:8px}
.socials i{width:26px;height:26px;border-radius:50%}
.sub-footer{left:0;top:2565px;width:1200px;height:126px;background:var(--footer-deep);color:#6d7a83;font-size:12.5px}
</style>
</head>
<body>
<div class="abs top-strip"></div>

<header class="abs header">
  <div class="abs brand"><span class="brand-mark"></span><span class="brand-name">Brightfold<br>Partners</span></div>
  <div class="abs contact-line" style="top:17px">daniel.hartley@brightfoldpartners.com.au
    <svg width="14" height="11" viewBox="0 0 14 11"><rect x="0.5" y="0.5" width="13" height="10" fill="none" stroke="#0b78d8"/><path d="M1 1l6 5 6-5" fill="none" stroke="#0b78d8"/></svg></div>
  <div class="abs contact-line" style="top:38px">+61 400 555 182
    <svg width="14" height="16" viewBox="0 0 10 16"><rect x="1" y="0.5" width="8" height="15" rx="1.5" fill="none" stroke="#0b78d8"/></svg></div>
  <nav class="abs nav">
    <a class="active" href="#">Home</a><a href="#">Our Mission</a><a href="#">Our Services</a><a href="#">About Us</a><a href="#" style="padding-right:0">Contact Us</a>
  </nav>
</header>

<section class="abs hero" role="img" aria-label="Industrial smokestacks releasing white smoke into a cloudy blue sky"></section>
<div class="abs hero-card">
  <p><b>W</b>e provides expert<br>advisory services in<br>Carbon Markets,<br>Climate Policy,<br>Landscapes and Change.</p>
  <div class="abs dots"><i></i><i></i><i></i><i class="on"></i></div>
</div>
<div class="abs hero-profile">
  <div class="portrait" role="img" aria-label="Portrait of the lead advisor"></div>
  <p><u>Daniel Hartley</u> is the lead advisor at<br>Brightfold Partners Advisory Services</p>
</div>

<div class="abs section-rule" style="top:724px"></div>
<div class="abs section-label" style="left:511px;top:707px;width:208px">Our Mission</div>
<p class="abs mission-text">Lorem Ipsum is simply dummy text of the printing and typesetting industry. Lorem Ipsum has been the industry's standard dummy text ever since the 1500s, when an unknown printer took a galley of type and scrambled it to make a type specimen book. It has survived not only five centuries, but also the leap into electronic typesetting, remaining essentially unchanged. It was popularised in the 1960s with the release of Typeline sheets containing Lorem Ipsum passages, and more recently with desktop publishing software like Pagewright Studio including versions of Lorem Ipsum.</p>
<div class="abs btn-ghost" style="left:552px;top:874px;width:116px">Read More...</div>

<div class="abs section-rule" style="top:961px"></div>
<div class="abs section-label" style="left:456px;top:945px;width:322px">Recent Engagements</div>

<article class="abs card" style="left:45px;top:1042px"><div class="photo" role="img" aria-label="Smokestacks against a blue sky" style="background:linear-gradient(#5f94cf,#c4d6e6)"></div><h3>Corporate Advisory on<br>Carbon Markets</h3></article>
<article class="abs card active" style="left:420px;top:1042px"><div class="photo" role="img" aria-label="Cooling towers emitting steam" style="background:linear-gradient(#2f5f9a,#d9dde2)"></div><h3>Project Mechanisms<br>(Carbon Credits &amp; Offsets)</h3></article>
<article class="abs card" style="left:793px;top:1042px"><div class="photo" role="img" aria-label="Engineer checking industrial gauges" style="background:linear-gradient(#6d7479,#3b4a57)"></div><h3>Monitoring, Reporting &amp; Verification</h3></article>
<article class="abs card" style="left:45px;top:1266px"><div class="photo" role="img" aria-label="Business team gathered around a table" style="background:linear-gradient(#c7c9cc,#6c7278)"></div><h3>Institutional Arrangements</h3></article>
<article class="abs card" style="left:420px;top:1266px"><div class="photo" role="img" aria-label="Trainees working at a lab bench" style="background:linear-gradient(#6f7b86,#2f3c48)"></div><h3>Training &amp; Coaching</h3></article>
<article class="abs card" style="left:793px;top:1266px"><div class="photo" role="img" aria-label="Power station chimneys and cooling towers" style="background:linear-gradient(#8fb1d6,#9a8d82)"></div><h3>China's Carbon Markets</h3></article>

<div class="abs section-rule" style="top:1550px"></div>
<div class="abs section-label" style="left:524px;top:1534px;width:165px">News</div>

<div class="abs news-photo" role="img" aria-label="Students examining equipment in a lab" style="left:47px;top:1611px;background:linear-gradient(#3d4a57,#8a939b)"></div>
<div class="abs news-body" style="left:210px;top:1626px"><h4>News Title One</h4>Lorem Ipsum is simply dummy text of the printing and typesetting industry. Lorem Ipsum has been the industry's standard dummy text ever since the 1500s, when an unknown printer took a galley of type and scrambled it to make a type specimen book. It has survived not only five<div class="btn-ghost">Read More...</div></div>
<div class="abs news-photo" role="img" aria-label="Red and white industrial chimneys" style="left:631px;top:1611px;background:linear-gradient(#7ea5cf,#b3a79c)"></div>
<div class="abs news-body" style="left:795px;top:1626px"><h4>News Title Two</h4>Lorem Ipsum is simply dummy text of the printing and typesetting industry. Lorem Ipsum has been the industry's standard dummy text ever since the 1500s, when an unknown printer took a galley of type and scrambled it to make a type specimen book. It has survived not only five<div class="btn-ghost">Read More...</div></div>

<section class="abs contact">
  <div class="abs" style="left:0;top:0;width:1200px;height:1px;background:var(--rule)"></div>
  <div class="abs field-label" style="left:45px;top:68px">Name</div>
  <div class="abs field" style="left:45px;top:86px;width:317px;height:34px"></div>
  <div class="abs field-label" style="left:440px;top:68px">Email</div>
  <div class="abs field" style="left:440px;top:86px;width:317px;height:34px"></div>
  <div class="abs field-label" style="left:834px;top:68px">Phone</div>
  <div class="abs field" style="left:834px;top:86px;width:318px;height:34px"></div>
  <div class="abs field-label" style="left:45px;top:140px">Message</div>
  <div class="abs field" style="left:45px;top:160px;width:1107px;height:106px"></div>
  <div class="abs btn-dark" style="left:536px;top:307px;width:140px">Submit</div>
</section>
<div class="abs section-label" style="left:511px;top:1905px;width:189px">Contact Us</div>

<footer class="abs footer">
  <div class="abs brand" style="left:45px;top:50px"><span class="brand-mark" style="background:#8593a0"></span><span class="brand-name">Brightfold<br>Partners</span></div>
  <div class="abs" style="left:111px;top:131px;width:290px;height:1px;background:#3d4b55"></div>
  <address class="abs" style="left:113px;top:146px;font-style:normal;font-size:12px;line-height:16px">Level 4, 120 Harbour Lane<br>Southbank Victoria 3006<br>Melbourne, Australia<br>Tel: +61 3 9000 4100<br>Fax: +61 3 9000 4199</address>
  <div class="abs" style="left:427px;top:66px"><h5>Who We Are</h5><ul><li>Home</li><li>Our Mission</li><li>About Us</li><li>Press Release</li><li>Contact Us</li></ul></div>
  <div class="abs" style="left:578px;top:66px"><h5>What We Do</h5><ul><li>Corporate Advisory on Carbon Market</li><li>Project Mechanisms (Carbon Credits &amp; Offsets)</li><li>Monitoring, Reporting &amp; Verification</li><li>Institutional Arrangements</li><li>Training &amp; Coaching</li><li>China's Carbon Markets</li></ul></div>
  <div class="abs" style="left:942px;top:66px;width:215px"><h5>Get Social</h5><p>Brightfold Partners is here, there and everywhere!<br>Follow us on your favourite social networking sites</p>
    <div class="socials" style="margin-top:8px"><i style="background:#3b5998"></i><i style="background:#1da1f2"></i><i style="background:#dd4b39"></i><i style="background:#0a77b5"></i><i style="background:#1ab7ea"></i></div></div>
</footer>

<div class="abs sub-footer">
  <div class="abs" style="left:113px;top:44px;display:flex;gap:24px;color:#9aa5ad">Sitemap<span style="border-left:1px solid #3d4b55;padding-left:24px">Privacy Policy</span></div>
  <div class="abs" style="left:113px;top:74px">Copyright © 2014 Brightfold Partners</div>
  <div class="abs" style="left:712px;top:30px">Subscribe Email Newsletter</div>
  <div class="abs" style="left:712px;top:56px;width:268px;height:32px;background:#7d878f;color:#2a343b;padding:8px 10px;font-size:12px">Email</div>
  <div class="abs" style="left:983px;top:56px;width:140px;height:32px;line-height:32px;background:var(--blue);color:var(--white);text-align:center;font-size:16px">Submit</div>
</div>
</body>
</html>
```